BRD business cards Dr. Martin Velk

I need a business card designed for our dental office. We are a "general dental" practice.
Looking for a clean, professional but not too fancy design with our logo and contact information required.
front of card is information/standard business card, backside is appt reminder with lines for date and time of appt
doctors name: Dr. Martin Velk DMD
office name: Velk Family Dental
address: 4827 E Tolland Ave Palm Hollow, FL 34021
phone: 954-555-0173
Dentistry
Office name, Doctor name, address, phone number...etc
- White/off white base color, blue and or black lettering

```html
<!DOCTYPE html>
<html lang="en">
<head>
<meta charset="utf-8">
<title>Velk Family Dental – Business Cards</title>
<link href="https://fonts.googleapis.com/css2?family=Cinzel:wght@500;600&family=Montserrat:wght@400;500&display=swap" rel="stylesheet">
<style>
  :root{
    --brand-blue:#1652a0;
    --ink:#1d1d1f;
    --rule:#8a8a8a;
    --card-white:#ffffff;
    --stage:#2a2a2b;
    --shadow:rgba(0,0,0,.45);
  }
  *{box-sizing:border-box;margin:0;padding:0}
  html,body{width:1200px;height:1186px;overflow:hidden}
  body{background:var(--stage);font-family:'Montserrat',sans-serif;position:relative}

  .card{position:absolute;left:220px;width:760px;height:434px;border-radius:30px;overflow:hidden;box-shadow:0 18px 40px var(--shadow)}
  .card--reminder{top:120px;background:var(--brand-blue)}
  .card--info{top:632px;background:var(--card-white)}

  /* wordmark */
  .wordmark{position:absolute;display:flex;align-items:center;gap:14px;font-family:'Cinzel',serif;font-weight:600;letter-spacing:.04em;line-height:1.1;white-space:nowrap}
  .wordmark__dot{width:28px;height:28px;border-radius:50%;flex:none}
  .wordmark--light{left:70px;top:60px;color:var(--card-white);font-size:32px}
  .wordmark--light .wordmark__dot{background:var(--card-white)}
  .wordmark--brand{left:70px;top:180px;color:var(--brand-blue);font-size:32px}
  .wordmark--brand .wordmark__dot{background:var(--brand-blue)}

  /* appointment panel */
  .appointment{position:absolute;left:22px;right:22px;top:176px;bottom:22px;background:var(--card-white);border-radius:18px;padding:22px 40px 0;color:var(--ink)}
  .appointment__title{text-align:center;font-family:'Cinzel',serif;font-weight:500;font-size:17px;letter-spacing:.05em;margin-bottom:28px}
  .field-row{display:flex;align-items:flex-end;gap:12px;margin-bottom:34px;font-size:16px}
  .field-row__label{flex:none}
  .field-row__line{flex:1;border-bottom:1.5px solid var(--rule);height:1px}
  .field-row__suffix{flex:none;font-size:15px}

  /* info side */
  .divider{position:absolute;left:400px;top:112px;width:2px;height:200px;background:var(--brand-blue)}
  .contact{position:absolute;left:428px;top:112px;color:var(--ink)}
  .contact__name{font-family:'Cinzel',serif;font-weight:600;font-size:25px;color:var(--brand-blue);letter-spacing:.02em;white-space:nowrap}
  .contact__role{font-size:17px;margin:2px 0 24px}
  .contact__item{display:flex;align-items:flex-start;gap:12px;font-size:16px;line-height:1.3;margin-bottom:12px;white-space:nowrap}
  .contact__icon{width:26px;height:26px;flex:none;margin-top:1px}
</style>
</head>
<body>

<section class="card card--reminder" aria-label="Appointment reminder side">
  <div class="wordmark wordmark--light"><span class="wordmark__dot"></span><span>Velk Family<br>Dental</span></div>
  <div class="appointment">
    <h2 class="appointment__title">YOUR NEXT APPOINTMENT</h2>
    <div class="field-row"><span class="field-row__label">Name</span><span class="field-row__line"></span></div>
    <div class="field-row"><span class="field-row__label">Date</span><span class="field-row__line"></span><span class="field-row__label">Time</span><span class="field-row__line"></span><span class="field-row__suffix">AM/PM</span></div>
    <div class="field-row"><span class="field-row__label">Note</span><span class="field-row__line"></span></div>
  </div>
</section>

<section class="card card--info" aria-label="Contact side">
  <div class="wordmark wordmark--brand"><span class="wordmark__dot"></span><span>Velk Family<br>Dental</span></div>
  <div class="divider"></div>
  <div class="contact">
    <h1 class="contact__name">Dr. Martin Velk DMD</h1>
    <p class="contact__role">Dentist</p>
    <p class="contact__item">
      <svg class="contact__icon" viewBox="0 0 26 26" aria-hidden="true"><circle cx="13" cy="13" r="13" fill="#1652a0"/><path d="M9.5 7.5l2 2.8-1.3 1.4c.8 1.7 2.2 3.1 3.9 3.9l1.4-1.3 2.8 2-1 1.8c-4.6-.4-8.6-4.4-9-9z" fill="#fff"/></svg>
      <span>954-555-0173</span>
    </p>
    <p class="contact__item">
      <svg class="contact__icon" viewBox="0 0 26 26" aria-hidden="true"><circle cx="13" cy="13" r="13" fill="#1652a0"/><path d="M13 6.5a4.5 4.5 0 0 0-4.5 4.5c0 3.3 4.5 8.5 4.5 8.5s4.5-5.2 4.5-8.5A4.5 4.5 0 0 0 13 6.5z" fill="#fff"/><circle cx="13" cy="11" r="1.7" fill="#1652a0"/></svg>
      <span>4827 E Tolland Ave<br>Palm Hollow, FL 34021</span>
    </p>
  </div>
</section>

</body>
</html>
```